Business Card Design

We just need these details on one side of card and logo on the other.

Industry/Entity Type

Business

Contact Information for Business Card

Lisel Pardoe | Artist
118 Coldwell Street
Malvern East Vic 3145
# 0412 978 205 | 03 9187 2604
lisel@liselpardoe.com
liselsnook.com.au

```html
<!DOCTYPE html>
<html lang="en">
<head>
<meta charset="utf-8">
<title>Lisel Pardoe – Business Card</title>
<link href="https://fonts.googleapis.com/css2?family=Lustria&display=swap" rel="stylesheet">
<style>
  :root {
    --bg: #9a9a9c;
    --card-dark: #1e1e1f;
    --card-mid: #333334;
    --orange: #f39419;
    --rule: #e8e8e8;
    --white: #f4f4f4;
  }
  * { margin: 0; padding: 0; box-sizing: border-box; }
  html, body { width: 1200px; height: 1000px; overflow: hidden; }
  body {
    background: radial-gradient(ellipse at 40% 40%, #b4b4b6 0%, var(--bg) 70%, #88888a 100%);
    font-family: "Lustria", Georgia, serif;
    position: relative;
  }
  .card {
    position: absolute;
    left: 220px;
    width: 760px;
    height: 400px;
    overflow: hidden;
    box-shadow: 0 10px 24px rgba(0,0,0,0.35);
  }
  .card--front { top: 70px; }
  .card--back { top: 520px; }
  .card__surface {
    position: absolute; inset: 0;
    background: linear-gradient(160deg, var(--card-mid) 0%, var(--card-dark) 75%);
  }
  .card__stripe {
    position: absolute; left: 0; right: 0; bottom: 0; height: 22px;
    background: var(--orange);
  }
  .rule { position: absolute; height: 2px; background: var(--rule); }

  /* contact side */
  .email {
    position: absolute; top: 36px; left: 0; right: 0;
    text-align: center; color: var(--orange); font-size: 24px;
  }
  .email-rule { top: 76px; left: 200px; width: 360px; }
  .email-icon { position: absolute; top: 82px; left: 366px; }
  .identity {
    position: absolute; top: 128px; left: 200px;
    display: flex; align-items: baseline; gap: 10px;
  }
  .identity__name { color: var(--orange); font-size: 40px; }
  .identity__role {
    color: var(--white); font-size: 22px;
    border-left: 2px solid var(--white); padding-left: 10px;
  }
  .address {
    position: absolute; top: 186px; left: 270px;
    color: var(--orange); font-size: 26px; line-height: 1.15;
  }
  .phone-icon { position: absolute; }
  .mobile-icon { top: 262px; left: 136px; }
  .mobile-rule { top: 300px; left: 60px; width: 250px; }
  .mobile { position: absolute; top: 308px; left: 62px; color: var(--orange); font-size: 28px; letter-spacing: 1px; }
  .landline-icon { top: 170px; left: 620px; }
  .landline-rule { top: 204px; left: 552px; width: 180px; }
  .landline { position: absolute; top: 212px; left: 556px; color: var(--orange); font-size: 24px; letter-spacing: 1px; }

  /* brand side */
  .brand {
    position: absolute; top: 108px; left: 0; right: 0;
    text-align: center; color: var(--orange); font-size: 92px; line-height: 1;
  }
  .tagline {
    position: absolute; top: 214px; left: 0; right: 0;
    text-align: center; color: var(--orange); font-size: 18px; letter-spacing: 4px;
  }
  .web-icon { position: absolute; top: 252px; left: 366px; }
  .web-rule { top: 280px; left: 240px; width: 280px; }
  .web { position: absolute; top: 290px; left: 0; right: 0; text-align: center; color: var(--orange); font-size: 24px; }
</style>
</head>
<body>

<section class="card card--front" aria-label="Business card, contact side">
  <div class="card__surface" role="img" aria-label="Dark charcoal wood-grain board texture"></div>

  <p class="email">lisel@liselpardoe.com</p>
  <div class="rule email-rule"></div>
  <svg class="email-icon" width="28" height="18" viewBox="0 0 28 18" aria-hidden="true">
    <rect x="1" y="1" width="26" height="16" fill="none" stroke="var(--orange)" stroke-width="1.6"/>
    <polyline points="1,1 14,10 27,1" fill="none" stroke="var(--orange)" stroke-width="1.6"/>
  </svg>

  <div class="identity">
    <span class="identity__name">Lisel Pardoe</span>
    <span class="identity__role">Artist</span>
  </div>
  <p class="address">118 Coldwell Street<br>Kellbrook East 3172</p>

  <svg class="phone-icon mobile-icon" width="20" height="32" viewBox="0 0 20 32" aria-hidden="true">
    <rect x="2" y="1" width="16" height="30" rx="3" fill="none" stroke="var(--orange)" stroke-width="2"/>
    <line x1="2" y1="25" x2="18" y2="25" stroke="var(--orange)" stroke-width="1.5"/>
    <circle cx="10" cy="28" r="1.3" fill="var(--orange)"/>
  </svg>
  <div class="rule mobile-rule"></div>
  <p class="mobile">0412 978 205</p>

  <svg class="phone-icon landline-icon" width="28" height="24" viewBox="0 0 28 24" aria-hidden="true">
    <rect x="4" y="2" width="14" height="20" rx="2" transform="rotate(-35 11 12)" fill="none" stroke="var(--orange)" stroke-width="2"/>
  </svg>
  <div class="rule landline-rule"></div>
  <p class="landline">03 9187 2604</p>

  <div class="card__stripe"></div>
</section>

<section class="card card--back" aria-label="Business card, brand side">
  <div class="card__surface" role="img" aria-label="Dark charcoal wood-grain board texture"></div>

  <p class="brand">Lisel's Nook</p>
  <p class="tagline">STUDIO · CAFE · GALLERY</p>

  <svg class="web-icon" width="26" height="26" viewBox="0 0 26 26" aria-hidden="true">
    <circle cx="13" cy="13" r="11" fill="none" stroke="var(--orange)" stroke-width="1.8"/>
    <ellipse cx="13" cy="13" rx="5" ry="11" fill="none" stroke="var(--orange)" stroke-width="1.4"/>
    <line x1="2" y1="13" x2="24" y2="13" stroke="var(--orange)" stroke-width="1.4"/>
  </svg>
  <div class="rule web-rule"></div>
  <p class="web">liselsnook.com.au</p>

  <div class="card__stripe"></div>
</section>

</body>
</html>
```